Quillory Nest Business Card

I need a business card design. We are a collaborate online training company. Our colors are gray and green. Our website is QuilloryNest.com

I would like an area for a profile picture within the card

```html
<!DOCTYPE html>
<html lang="en">
<head>
<meta charset="utf-8">
<title>Quillory Nest Business Card</title>
<link href="https://fonts.googleapis.com/css2?family=Didact+Gothic&family=Exo+2:wght@500&family=PT+Sans+Narrow:wght@700&display=swap" rel="stylesheet">
<style>
  :root {
    --stage: #9a9c9b;
    --paper: #ffffff;
    --green-1: #8cc63f;
    --green-2: #7dbb2f;
    --green-3: #6fa52c;
    --green-4: #54892a;
    --green-light: #95c42e;
    --gray-text: #7a7a7a;
    --ink: #2b2b2b;
    --soft: #b4b4b4;
  }
  html, body { margin: 0; padding: 0; overflow: hidden; }
  body {
    width: 1200px; height: 1200px;
    background: var(--stage);
    position: relative;
    font-family: "Exo 2", sans-serif;
  }
  .card {
    position: absolute; left: 176px; width: 848px; height: 469px;
    background: var(--paper); border-radius: 7px; overflow: hidden;
    box-shadow: 0 0 0 2px rgba(255,255,255,0.12);
  }
  .card--front { top: 96px; }
  .card--back { top: 634px; height: 468px; }
  .tile { position: absolute; }
  .g1 { background: var(--green-1); }
  .g2 { background: var(--green-2); }
  .g3 { background: var(--green-3); }
  .g4 { background: var(--green-4); }

  .wordmark {
    position: absolute; display: flex; align-items: center; gap: 16px;
    font-family: "PT Sans Narrow", sans-serif; font-weight: 700;
    color: var(--gray-text); white-space: nowrap; letter-spacing: -1px;
    line-height: 1;
  }
  .wordmark__dot { border-radius: 50%; background: var(--green-1); flex: none; }
  .front-mark { left: 0; right: 0; top: 180px; justify-content: center; font-size: 66px; }
  .front-mark .wordmark__dot { width: 56px; height: 56px; }
  .front-url {
    position: absolute; left: 0; right: 0; top: 432px; text-align: center;
    font-family: "Didact Gothic", sans-serif; font-size: 21px; line-height: 26px; color: var(--soft);
  }

  .back-panel { position: absolute; left: 0; top: 0; width: 427px; height: 100%; background: var(--green-2); }
  .photo-frame {
    position: absolute; left: 112px; top: 59px; width: 156px; height: 157px;
    background: var(--green-3); border-radius: 5px; padding: 5px; box-sizing: border-box;
  }
  .photo {
    width: 100%; height: 100%; border-radius: 3px;
    background: linear-gradient(160deg, #e2e2e2 0%, #b9b9b9 55%, #4a4a4a 100%);
  }
  .photo-bar { position: absolute; left: 112px; top: 222px; height: 7px; display: flex; }
  .photo-bar span { width: 39px; height: 100%; }
  .chat-icon { position: absolute; left: 280px; top: 220px; }
  .person-name {
    position: absolute; left: 105px; top: 238px;
    font-family: "Didact Gothic", sans-serif; font-size: 34px; line-height: 40px; color: var(--ink);
  }
  .person-role {
    position: absolute; left: 190px; top: 276px;
    font-family: "Didact Gothic", sans-serif; font-size: 22px; line-height: 26px; color: #f2f8e8;
  }
  .back-mark { left: 448px; top: 96px; font-size: 58px; }
  .back-mark .wordmark__dot { width: 50px; height: 50px; }
  .contact { position: absolute; left: 401px; display: flex; align-items: flex-start; gap: 12px; }
  .contact__icon {
    width: 38px; height: 38px; border-radius: 5px; background: var(--green-4);
    display: flex; align-items: center; justify-content: center; flex: none;
  }
  .contact__text { font-size: 23px; line-height: 31px; color: var(--ink); padding-top: 3px; white-space: nowrap; }
  .base-line { position: absolute; left: 0; bottom: 0; width: 100%; height: 4px; background: var(--green-4); }
</style>
</head>
<body>
  <section class="card card--front">
    <div class="tile g2" style="left:0;top:0;width:59px;height:47px"></div>
    <div class="tile g3" style="left:0;top:47px;width:59px;height:56px"></div>
    <div class="tile g4" style="left:0;top:103px;width:59px;height:56px"></div>
    <div class="tile g4" style="right:0;top:311px;width:59px;height:56px"></div>
    <div class="tile g3" style="right:0;top:367px;width:59px;height:56px"></div>
    <div class="tile g2" style="right:0;top:423px;width:59px;height:46px"></div>
    <div class="wordmark front-mark"><span class="wordmark__dot"></span>Quillory Nest</div>
    <div class="front-url">www.quillorynest.com</div>
  </section>

  <section class="card card--back">
    <div class="back-panel">
      <div class="photo-frame"><div class="photo" role="img" aria-label="Profile photo of the founder"></div></div>
      <div class="photo-bar"><span class="g1"></span><span class="g2"></span><span class="g3"></span><span class="g4"></span></div>
      <svg class="chat-icon" width="40" height="24" viewBox="0 0 40 24">
        <rect x="1" y="1" width="37" height="17" rx="2" fill="none" stroke="#fff" stroke-width="1.5"/>
        <path d="M6 18 L6 23 L11 18" fill="none" stroke="#fff" stroke-width="1.5"/>
        <circle cx="13" cy="10" r="1.8" fill="#fff"/><circle cx="20" cy="10" r="1.8" fill="#fff"/><circle cx="27" cy="10" r="1.8" fill="#fff"/>
      </svg>
      <div class="person-name">Dorian Pell</div>
      <div class="person-role">Founder</div>
      <div class="tile" style="left:0;top:414px;width:97px;height:50px;background:var(--green-light)"></div>
      <div class="tile g2" style="left:97px;top:414px;width:109px;height:50px"></div>
      <div class="tile g3" style="left:206px;top:414px;width:110px;height:50px"></div>
      <div class="tile g4" style="left:316px;top:414px;width:111px;height:50px"></div>
    </div>
    <div class="tile g2" style="left:408px;top:0;width:22px;height:30px"></div>
    <div class="tile g3" style="left:408px;top:30px;width:22px;height:30px"></div>
    <div class="tile g4" style="left:408px;top:60px;width:22px;height:30px"></div>

    <div class="wordmark back-mark"><span class="wordmark__dot"></span>Quillory Nest</div>

    <div class="contact" style="top:236px">
      <div class="contact__icon">
        <svg width="22" height="22" viewBox="0 0 24 24"><path fill="#fff" d="M6.6 10.8a15 15 0 0 0 6.6 6.6l2.2-2.2c.3-.3.7-.4 1-.2 1.1.4 2.3.6 3.6.6.6 0 1 .4 1 1V20c0 .6-.4 1-1 1A17 17 0 0 1 3 4c0-.6.4-1 1-1h3.5c.6 0 1 .4 1 1 0 1.3.2 2.5.6 3.6.1.3 0 .7-.2 1z"/></svg>
      </div>
      <div class="contact__text">(302) 555-0147</div>
    </div>
    <div class="contact" style="top:300px">
      <div class="contact__icon">
        <svg width="20" height="24" viewBox="0 0 20 24"><path fill="#fff" d="M10 1a7.5 7.5 0 0 0-7.5 7.5C2.5 14 10 23 10 23s7.5-9 7.5-14.5A7.5 7.5 0 0 0 10 1zm0 10.5a3 3 0 1 1 0-6 3 3 0 0 1 0 6z"/></svg>
      </div>
      <div class="contact__text" style="padding-top:-4px;margin-top:-6px">4870 W Alder Blvd. Suite 12<br>Harlow, Arizona 85990</div>
    </div>
    <div class="contact" style="top:360px">
      <div class="contact__icon">
        <svg width="22" height="22" viewBox="0 0 24 24" fill="none" stroke="#fff" stroke-width="2.4" stroke-linecap="round"><circle cx="5" cy="19" r="1.6" fill="#fff" stroke="none"/><path d="M4 11a9 9 0 0 1 9 9"/><path d="M4 4a16 16 0 0 1 16 16"/></svg>
      </div>
      <div class="contact__text">www.quillorynest.com</div>
    </div>
    <div class="base-line"></div>
  </section>
</body>
</html>
```